Financing company needs a 1-page website with contact form

We are a financing company focusing on manufacturing sector. We need a simple 1 page website with contact form that is consistent and aligned to the main website (it is part of a bigger company). Please adhere to the same color scheme to make it look similar, but not necessarily a carbon copy.

Website link www.orvalcapital.net

I also need the designer to suggest stock images that are suitable (related to manufacturing sector).

Files to be in html format.

Font: Try to match the main website or use a simple, sans serif font that is similar

Reason: Dear designers, thank you for your submissions. I believe I have given my feedback to all of you. But we would like to extend it by a few days to give a chance for more designers to join, and tweak the existing submissions. Thanks!

Target Market(s)

Small and medium companies in manufacturing sector, potential investors

Industry/Entity Type

Financial Service

Font styles to use
Sans Serif

Requirements
Must have
• Consistency to the main website www.orvalcapital.net
• Can use simialr layout too to make it easier
• Contact form
• to have a one page website like this example https://www.trylumo.com/

```html
<!DOCTYPE html>
<html lang="en">
<head>
<meta charset="utf-8">
<title>Altamar Factoring</title>
<link href="https://fonts.googleapis.com/css2?family=Open+Sans:wght@400;600;700;800&display=swap" rel="stylesheet">
<style>
:root{
  --red:#c1272d;
  --ink:#333333;
  --muted:#8a8a8a;
  --light:#f1f1f1;
  --footer:#2c2c2c;
  --footer-deep:#1f1f1f;
}
*{box-sizing:border-box;margin:0;padding:0}
html,body{width:1200px;height:2332px;overflow:hidden}
body{font-family:"Open Sans",Arial,sans-serif;color:var(--ink);background:#fff}
.site-header{height:60px;display:flex;align-items:center;justify-content:space-between;padding:0 36px;background:#fff}
.brand{font-weight:700;font-size:22px;letter-spacing:.5px;color:var(--ink)}
.main-nav{display:flex;gap:34px;font-size:12px;font-weight:600;letter-spacing:.6px}
.main-nav a{color:var(--ink);text-decoration:none;padding:6px 10px}
.main-nav a.active{background:var(--red);color:#fff}
.hero{position:relative;height:532px;background:linear-gradient(120deg,#cfd6dc 0%,#aeb8c1 40%,#6f7780 75%,#4b525a 100%)}
.hero-caption{position:absolute;left:34px;top:222px;width:470px;padding:20px 22px;background:rgba(30,30,30,.55);color:#fff;font-size:25px;font-weight:700;line-height:1.3}
.hero-dots{position:absolute;left:40px;bottom:22px;display:flex;gap:8px}
.hero-dots span{width:9px;height:9px;border-radius:50%;background:rgba(255,255,255,.5)}
.hero-dots span:first-child{background:#fff}
.section{text-align:center;padding:0 140px}
.section-mark{width:14px;height:14px;background:var(--red);margin:0 auto 14px}
.section h2{font-size:30px;font-weight:800;letter-spacing:2px;color:var(--ink);margin-bottom:22px}
.section p{font-size:12px;line-height:1.75;color:var(--muted)}
.about{height:220px;padding-top:28px}
.services{height:262px;padding-top:34px;background:var(--light)}
.personnel{height:490px;padding-top:34px}
.personnel p{text-align:left}
.focus-list{list-style:none;margin:26px 0 0 400px;text-align:left}
.focus-list li{display:flex;align-items:center;gap:14px;height:52px;font-size:12px;color:var(--ink)}
.staff{height:256px;padding-top:30px;background:var(--light)}
.staff h2{margin-bottom:16px}
.staff-grid{display:flex;justify-content:space-between;gap:40px}
.member{width:280px}
.member h3{font-size:14px;font-weight:600;color:var(--ink)}
.member .role{font-size:11px;color:var(--muted);margin:4px 0 8px}
.member p{font-size:11px;line-height:1.6}
.site-footer{height:470px;background:var(--footer);color:#e6e6e6;display:flex;padding:36px 70px 0}
.contact{width:490px}
.site-footer h2{font-size:28px;font-weight:700;letter-spacing:1.5px;color:#fff;margin-bottom:22px}
.offices{display:flex;gap:60px;font-size:11px;line-height:1.65;color:#bdbdbd}
.offices strong{display:block;color:#fff;font-size:12px;margin-bottom:2px}
.offices .label{color:#fff;margin-top:8px;display:block}
.group-note{margin-top:150px;font-size:22px;font-weight:600;color:#fff}
.enquiry{flex:1}
.form-row{display:flex;gap:16px;margin-bottom:16px}
.field{flex:1;height:38px;border:1px solid #555;background:#3a3a3a;color:#9a9a9a;font-size:11px;padding:11px 12px}
.field.comments{height:130px}
.submit{display:block;margin-left:auto;background:var(--red);color:#fff;border:0;font-family:inherit;font-size:11px;font-weight:700;letter-spacing:1px;padding:12px 22px;margin-top:40px}
.copyright{height:42px;background:var(--footer-deep);color:#8c8c8c;font-size:10px;padding:15px 70px}
</style>
</head>
<body>
<header class="site-header">
  <div class="brand">ALTAMAR</div>
  <nav class="main-nav">
    <a class="active" href="#">HOME</a><a href="#">WHO ARE WE?</a><a href="#">OUR SERVICES</a><a href="#">KEY PERSONNEL</a><a href="#">CONTACT US</a>
  </nav>
</header>

<section class="hero" role="img" aria-label="Photo of business people smiling in a bright office meeting">
  <div class="hero-caption">Altamar Factoring is a specialist financier focusing on small and medium-sized enterprises (SMEs) in emerging markets.</div>
  <div class="hero-dots"><span></span><span></span><span></span></div>
</section>

<section class="section about">
  <div class="section-mark"></div>
  <h2>WHO ARE WE?</h2>
  <p>Altamar Factoring is a specialist financier focusing on small and medium-sized enterprises (SMEs) in emerging markets. We provide working capital, typically in structured trade finance, to businesses in the manufacturing and retail sectors.</p>
  <p style="margin-top:10px">We are supported by a team of highly experienced professionals with in-depth knowledge of credit, private equity and investment.</p>
</section>

<section class="section services">
  <div class="section-mark"></div>
  <h2>OUR SERVICES</h2>
  <p>Our key focus is on companies in the manufacturing sector that are in need of working capital. We meet their financing needs by developing structured offerings after a careful analysis of the companies' operations and processes. Our business model is based on structured lending in the form of trade finance facilities. How we are different is the way we combine a lean practice, insurance discipline with our experience in trade finance structuring.</p>
</section>

<section class="section personnel">
  <div class="section-mark"></div>
  <h2>KEY PERSONNEL</h2>
  <p>Our key focus is on companies in the manufacturing sector that are in need of working capital. We meet their financing needs by developing structured offerings after a careful analysis of the companies' operations and processes. Our business model is based on structured lending in the form of trade finance facilities. How we are different is the way we combine a lean practice, insurance discipline with our experience in trade finance structuring.</p>
  <ul class="focus-list">
    <li><svg width="16" height="16" viewBox="0 0 16 16"><rect width="16" height="16" fill="#c1272d"/><path d="M4 8.5l2.6 2.5L12 5.5" stroke="#fff" stroke-width="2" fill="none"/></svg>Private equity &amp; innovative deals</li>
    <li><svg width="16" height="16" viewBox="0 0 16 16"><rect width="16" height="16" fill="#c1272d"/><path d="M4 8.5l2.6 2.5L12 5.5" stroke="#fff" stroke-width="2" fill="none"/></svg>Islamic financing structures</li>
    <li><svg width="16" height="16" viewBox="0 0 16 16"><rect width="16" height="16" fill="#c1272d"/><path d="M4 8.5l2.6 2.5L12 5.5" stroke="#fff" stroke-width="2" fill="none"/></svg>SME credits, factoring and leasing</li>
    <li><svg width="16" height="16" viewBox="0 0 16 16"><rect width="16" height="16" fill="#c1272d"/><path d="M4 8.5l2.6 2.5L12 5.5" stroke="#fff" stroke-width="2" fill="none"/></svg>Turnaround accounting, debt and cash collection</li>
    <li><svg width="16" height="16" viewBox="0 0 16 16"><rect width="16" height="16" fill="#c1272d"/><path d="M4 8.5l2.6 2.5L12 5.5" stroke="#fff" stroke-width="2" fill="none"/></svg>SME management and advisory</li>
  </ul>
</section>

<section class="section staff">
  <div class="section-mark"></div>
  <h2>OUR STAFF</h2>
  <div class="staff-grid">
    <div class="member"><h3>Selim Arkan</h3><div class="role">Managing Partner</div><p>Selim brings a long career in investment banking and trade finance, with deep ties across regional markets and lending networks.</p></div>
    <div class="member"><h3>Deniz Ulusoy</h3><div class="role">Managing Partner</div><p>Deniz has extensive experience in special situations, restructuring and credit analysis for SME clients across sectors.</p></div>
    <div class="member"><h3>Marin Petrescu</h3><div class="role">Manager</div><p>Marin is responsible for overseeing origination and portfolio management, with a focus on structured trade finance.</p></div>
  </div>
</section>

<footer class="site-footer">
  <div class="contact">
    <h2>CONTACT US</h2>
    <div class="offices">
      <div><strong>Turkey</strong>Levent Plaza No. 12<br>Besiktas 34330, Istanbul<br>Turkey<span class="label">Phone</span>+90 212 555 0148</div>
      <div><strong>Hong Kong</strong>Suite 1204, Harbour Tower<br>88 Gloucester Road<br>Wan Chai, Hong Kong<span class="label">A member of Orval Group</span></div>
    </div>
    <div class="group-note">A member of Orval Group</div>
  </div>
  <div class="enquiry">
    <h2>ENQUIRY FORM</h2>
    <div class="form-row"><div class="field">Name</div><div class="field">Phone Number</div></div>
    <div class="form-row"><div class="field">Email Address</div></div>
    <div class="form-row"><div class="field comments">Comments / Message</div></div>
    <button class="submit">SUBMIT NOW</button>
  </div>
</footer>
<div class="copyright">© 2016 Orval Group. All rights reserved.</div>
</body>
</html>
```